VornaDerm/The experts in permanent hairremoval

Our Brand is VornaDerm and we are specialized on permantent hair removal for the body for men and woman. VornaDerm is working as a Franchise chain.
The brand should be positioned as lifestyle brand but with a medical background. People should trust in us. We take care about their body. This need to be communicated 100%.
Our system is inexpensive but we don't want to show that we are cheap. So we want to communicate that permanent hair removal is a real lifestyle product but affordable.
We already created a logo that you can see the style and colour we prefer.

Target Market(s)

Europe beginning (especially german spoken markets), Middle East, Africa

Industry/Entity Type

Hair Removal

Number of Pages Required

5+ page

Font styles to use
Serif
Other font styles liked:
• Trajan Pro

Requirements
Nice to have
• We are very open for new ideas

```html
<!DOCTYPE html>
<html lang="en">
<head>
<meta charset="utf-8">
<title>VornaDerm – Our Studios</title>
<link href="https://fonts.googleapis.com/css2?family=Alegreya+Sans:wght@300;400;500&display=swap" rel="stylesheet">
<style>
:root{
  --teal:#2f86a8;
  --blue:#4fa9df;
  --sky:#57b2e6;
  --page:#f2f2f4;
  --panel-head:#e4e5e7;
  --line:#d6d7da;
  --text:#666a70;
  --text-dark:#55595e;
  --white:#ffffff;
  --map-a:#0f5f86;
  --map-b:#1b79a3;
}
*{box-sizing:border-box;margin:0;padding:0}
html,body{width:1142px;height:1200px;overflow:hidden}
body{font-family:'Alegreya Sans',sans-serif;background:var(--page);color:var(--text);position:relative}
.topbar{position:absolute;left:0;top:0;width:1142px;height:48px;background:var(--teal);color:#a9dcf2;font-size:13.5px;font-weight:300}
.topbar .note{position:absolute;left:49px;top:15px}
.topbar .note b{color:var(--white);font-weight:500}
.topbar .contact{position:absolute;top:14px;color:var(--white);display:flex;align-items:center;gap:8px;font-weight:400}
.header{position:absolute;top:48px;left:0;width:1142px;height:164px;border-bottom:1px solid var(--line)}
.brand{position:absolute;left:49px;top:62px;display:flex;align-items:center;gap:12px}
.brand .dot{width:36px;height:36px;border-radius:50%;background:var(--blue)}
.brand .name{font-size:38px;font-weight:400;color:#7a7e84;letter-spacing:.5px}
.nav{position:absolute;right:47px;top:72px;display:flex;gap:16px;font-size:15.5px;font-weight:400;color:var(--text-dark)}
.nav .active{color:var(--blue);position:relative}
.nav .active::after{content:"";position:absolute;left:0;right:0;top:73px;height:2px;background:var(--blue)}
.nav svg{margin-left:6px;margin-top:-1px}
.title{position:absolute;top:242px;width:1142px;text-align:center;font-size:37px;font-weight:300;color:var(--text);letter-spacing:.5px}
.price-panel{position:absolute;left:54px;top:311px;width:1044px;height:292px;background:var(--white);border:1px solid var(--line)}
.price-panel .head{height:50px;background:var(--panel-head);border-bottom:1px solid var(--line);padding:14px 33px;font-size:19px;color:var(--text-dark)}
.select{position:absolute;left:162px;top:82px;width:205px;height:50px;border:1px solid #8f9399;font-size:13px;color:#a4a7ab;padding:16px 24px}
.select svg{position:absolute;right:32px;top:20px}
.options{position:absolute;left:162px;top:132px;width:205px;height:127px;background:var(--sky);padding:14px 24px;font-size:13.5px;color:#d5ecf9;line-height:20.3px}
.options .current{color:var(--white)}
.options .bar{position:absolute;right:9px;top:16px;width:5px;height:34px;background:var(--white);border-radius:2px}
.detail{position:absolute;left:473px;top:78px;width:420px}
.detail h2{font-size:20px;font-weight:400;color:var(--text-dark);margin-bottom:8px}
.detail p{font-size:12px;line-height:16.5px;color:var(--text)}
.detail .price{margin-top:12px;font-size:12.5px;color:var(--text-dark)}
.detail .price span{color:var(--blue)}
.divider{position:absolute;left:0;top:635px;width:1142px;height:1px;background:var(--line)}
.info{position:absolute;top:665px;width:300px}
.info .label{display:flex;align-items:center;gap:14px;font-size:23px;font-weight:400;color:var(--text)}
.info .value{margin-top:10px;font-size:19px;font-weight:300;color:var(--blue);line-height:26px}
.map{position:absolute;left:0;top:792px;width:1142px;height:326px;background:linear-gradient(135deg,var(--map-b),var(--map-a) 55%,#0b4c6e)}
.footer{position:absolute;left:0;top:1118px;width:1142px;height:82px;background:var(--teal);color:var(--white)}
.footer .copy{position:absolute;left:49px;top:35px;font-size:14px;font-weight:400}
.social{position:absolute;left:743px;top:22px;display:flex;gap:31px}
.social .ring{width:34px;height:34px;border:2px solid var(--white);border-radius:50%;display:flex;align-items:center;justify-content:center}
.social .ring.soft{border-color:#8fc8e4}
.to-top{position:absolute;right:49px;top:27px}
</style>
</head>
<body>
<div class="topbar">
  <div class="note">One of our representatives will happily contact you within <b>24 hours.</b> For urgent needs call us at</div>
  <div class="contact" style="left:737px">
    <svg width="18" height="18" viewBox="0 0 24 24"><path fill="#8fd0f2" d="M6.6 10.8a15 15 0 0 0 6.6 6.6l2.2-2.2c.3-.3.7-.4 1-.2 1.1.4 2.3.6 3.6.6.6 0 1 .4 1 1V20c0 .6-.4 1-1 1A17 17 0 0 1 3 4c0-.6.4-1 1-1h3.5c.6 0 1 .4 1 1 0 1.3.2 2.5.6 3.6.1.3 0 .7-.2 1z"/></svg>
    800-555-0142
  </div>
  <div class="contact" style="left:888px">
    <svg width="28" height="17" viewBox="0 0 28 17"><rect width="28" height="17" fill="#7fc4ea"/><path d="M1 1l13 9 13-9M1 16l9-7M27 16l-9-7" stroke="#fff" stroke-width="1.3" fill="none"/></svg>
    hello@vornaderm-mail.com
  </div>
</div>

<header class="header">
  <div class="brand"><span class="dot"></span><span class="name">VornaDerm</span></div>
  <nav class="nav">
    <span>HOME</span><span class="active">STUDIOS</span><span>WHY CHOOSE THIS</span><span>FRANCHISE</span><span>ABOUT</span><span>CONTACT</span><span>ONLINE SHOP</span>
    <svg width="22" height="22" viewBox="0 0 22 22"><circle cx="9" cy="9" r="7" stroke="#4fa9df" stroke-width="3" fill="none"/><path d="M14 14l6 6" stroke="#4fa9df" stroke-width="3.5" stroke-linecap="round"/></svg>
  </nav>
</header>

<h1 class="title">OUR STUDIOS</h1>

<section class="price-panel">
  <div class="head">PRICE LIST</div>
  <div class="select">Select country
    <svg width="13" height="8" viewBox="0 0 13 8"><path d="M1 1l5.5 5.5L12 1" stroke="#666" stroke-width="1.5" fill="none"/></svg>
  </div>
  <div class="options">
    <div>Country 01</div><div class="current">Country 02</div><div>Country 03</div><div>Country 04</div><div>Country 05</div>
    <span class="bar"></span>
  </div>
  <div class="detail">
    <h2>COUNTRY 01</h2>
    <p>This is some description, if needed. (dummy text)<br>Our hair clinic office provides personalized hair care to everyone. Our entire team is&nbsp; dedicated to providing you with the highest</p>
    <div class="price">PRICE:&nbsp; <span>$00.00</span></div>
  </div>
</section>

<div class="divider"></div>

<div class="info" style="left:78px">
  <div class="label" style="margin-left:66px">
    <svg width="22" height="34" viewBox="0 0 22 34"><path d="M11 0a11 11 0 0 0-11 11c0 8 11 20 11 20s11-12 11-20A11 11 0 0 0 11 0z" fill="#4fa9df"/><circle cx="11" cy="11" r="4" fill="#f2f2f4"/><ellipse cx="11" cy="32" rx="7" ry="2" fill="#4fa9df"/></svg>
    ADDRESS
  </div>
  <div class="value">27 Linden Row, Harbourton,<br>D04 5KT</div>
</div>
<div class="info" style="left:443px">
  <div class="label" style="margin-left:60px">
    <svg width="34" height="34" viewBox="0 0 24 24"><path fill="#4fa9df" d="M6.6 10.8a15 15 0 0 0 6.6 6.6l2.2-2.2c.3-.3.7-.4 1-.2 1.1.4 2.3.6 3.6.6.6 0 1 .4 1 1V20c0 .6-.4 1-1 1A17 17 0 0 1 3 4c0-.6.4-1 1-1h3.5c.6 0 1 .4 1 1 0 1.3.2 2.5.6 3.6.1.3 0 .7-.2 1z"/></svg>
    CALL US
  </div>
  <div class="value">800-555-0142 ; 800-555-0142</div>
</div>
<div class="info" style="left:809px">
  <div class="label" style="margin-left:37px">
    <svg width="54" height="33" viewBox="0 0 28 17"><rect width="28" height="17" fill="#4fa9df"/><path d="M1 1l13 9 13-9M1 16l9-7M27 16l-9-7" stroke="#fff" stroke-width="1.2" fill="none"/></svg>
    EMAIL US
  </div>
  <div class="value">hello@vornaderm-mail.com</div>
</div>

<div class="map" role="img" aria-label="Street map showing the studio location"></div>

<footer class="footer">
  <div class="copy">© COPYRIGHT 2015. VORNADERM. ALL RIGHTS RESERVED.</div>
  <div class="social">
    <span class="ring" aria-label="Social profile"></span>
    <span class="ring soft" aria-label="Social profile"></span>
    <span class="ring soft" aria-label="Social profile"></span>
    <span class="ring soft" aria-label="Email">
      <svg width="15" height="10" viewBox="0 0 15 10"><rect x=".5" y=".5" width="14" height="9" fill="none" stroke="#8fc8e4"/><path d="M1 1l6.5 5L14 1" stroke="#8fc8e4" fill="none"/></svg>
    </span>
  </div>
  <svg class="to-top" width="56" height="28" viewBox="0 0 56 28"><path d="M2 26L28 3l26 23" stroke="#fff" stroke-width="5" fill="none"/></svg>
</footer>
</body>
</html>
```